ADA COMPLIANCE

We are in need of flyer or tri fold page for ada compliance, handicap ramps and parking lot striping.

Target Market(s)

Commercial Construction Industry

Industry/Entity Type

Parking

Font styles to use
Other font styles liked:
• Felix Titling

Colors
0355a3
acd036

Requirements
Must have
• Our Company Name and logo, 8005172943 number License #2004738
• List of services provided in uploaded images. Navy blue with high vizability green

```html
<!DOCTYPE html>
<html lang="en">
<head>
<meta charset="utf-8">
<title>Summit Build – ADA Compliance Tri-Fold</title>
<link href="https://fonts.googleapis.com/css2?family=Cinzel:wght@600;700&family=Lato:wght@400;700&display=swap" rel="stylesheet">
<style>
  :root{
    --navy:#0355a3;
    --navy-deep:#0a2f7a;
    --green:#acd036;
    --green-light:#c8e65a;
    --paper:#f2f2f2;
    --paper-shade:#dedede;
    --ink:#1d1d1d;
    --white:#ffffff;
  }
  *{box-sizing:border-box;margin:0;padding:0}
  html,body{width:1200px;height:1200px;overflow:hidden;background:var(--white)}
  body{position:relative;font-family:'Lato',sans-serif;color:var(--ink)}

  .sheet{position:absolute;left:244px;width:712px;height:503px;overflow:hidden;
    background:linear-gradient(135deg,var(--paper) 0%,#fafafa 45%,var(--paper-shade) 100%)}
  .sheet--outside{top:51px}
  .sheet--inside{top:611px}
  .sheet__art{position:absolute;inset:0;width:712px;height:503px}

  .tab{position:absolute;height:28px;display:flex;align-items:center;padding-left:28px;
    font-family:'Cinzel',serif;font-weight:700;font-size:14px;letter-spacing:1px;border-radius:0 14px 14px 0}
  .tab--green{background:linear-gradient(var(--green-light),var(--green));color:var(--navy-deep);width:139px}
  .tab--navy{background:linear-gradient(#1a4fb0,var(--navy-deep));color:var(--white);width:134px;padding-left:24px}

  .copy{position:absolute;width:184px;font-size:9.4px;line-height:11.2px;letter-spacing:.2px}

  .contact{position:absolute;left:265px;width:182px;text-align:center;font-size:11px;line-height:14px}
  .contact__title{font-family:'Cinzel',serif;font-weight:700;font-size:17px;color:var(--navy-deep);
    text-decoration:underline;text-underline-offset:3px;margin-bottom:8px;letter-spacing:.5px}
  .contact p{margin-bottom:6px}

  .brand{position:absolute;left:486px;top:100px;width:216px;display:flex;align-items:center;justify-content:center;gap:8px;
    font-family:'Lato',sans-serif;font-weight:700;font-size:24px;line-height:28px;color:var(--navy-deep);letter-spacing:.5px}
  .brand__mark{width:16px;height:16px;background:var(--navy-deep);flex:none}

  .cover-title{position:absolute;left:477px;top:436px;width:235px;text-align:center;font-family:'Cinzel',serif;
    font-weight:700;font-size:24px;color:var(--green)}
  .cover-web{position:absolute;left:477px;top:468px;width:235px;text-align:center;font-size:9px;letter-spacing:2px;color:var(--white);font-weight:700}

  .feature-title{position:absolute;left:238px;top:30px;width:236px;text-align:center;font-family:'Cinzel',serif;
    font-weight:700;font-size:26px;color:var(--navy-deep)}
  .back-contact{position:absolute;left:238px;width:236px;text-align:center}
  .back-contact__title{top:434px;font-family:'Cinzel',serif;font-weight:700;font-size:21px;color:var(--green);
    text-decoration:underline;text-underline-offset:3px}
  .back-contact__phone{top:464px;font-size:16px;color:var(--white)}
</style>
</head>
<body>

<section class="sheet sheet--outside">
  <svg class="sheet__art" viewBox="0 0 712 503" xmlns="http://www.w3.org/2000/svg">
    <defs>
      <linearGradient id="greenPanel" x1="0" y1="0" x2="1" y2="1">
        <stop offset="0" stop-color="#c6e84e"/><stop offset="1" stop-color="#93c22c"/>
      </linearGradient>
      <linearGradient id="navyFill" x1="0" y1="0" x2="1" y2="1">
        <stop offset="0" stop-color="#0a2f7a"/><stop offset="1" stop-color="#0355a3"/>
      </linearGradient>
      <linearGradient id="photoLot" x1="0" y1="0" x2="0" y2="1">
        <stop offset="0" stop-color="#8fb5dc"/><stop offset=".45" stop-color="#c9b39a"/><stop offset="1" stop-color="#2d3640"/>
      </linearGradient>
      <linearGradient id="photoStairs" x1="0" y1="0" x2="0" y2="1">
        <stop offset="0" stop-color="#9aa4ad"/><stop offset="1" stop-color="#c9c9c4"/>
      </linearGradient>
      <linearGradient id="photoPerson" x1="0" y1="0" x2="0" y2="1">
        <stop offset="0" stop-color="#e9e9e9"/><stop offset=".35" stop-color="#cfa98d"/><stop offset="1" stop-color="#1d1f24"/>
      </linearGradient>
    </defs>

    <path d="M237,0 H475 V135 C420,150 300,170 237,150 Z" fill="url(#greenPanel)"/>

    <path d="M0,0 H237 V255 C170,230 60,210 0,100 Z" fill="url(#photoLot)" role="img" aria-label="Photo of a commercial building with a freshly striped accessible parking lot"/>
    <path d="M0,100 C60,215 170,235 237,258 C275,275 300,300 304,334 C296,300 270,285 237,275 C150,250 30,230 0,130 Z" fill="url(#navyFill)"/>
    <path d="M237,150 C300,170 420,150 475,125 V140 C420,170 330,190 260,180 Z" fill="url(#navyFill)"/>

    <circle cx="360" cy="187" r="90" fill="url(#navyFill)"/>
    <circle cx="360" cy="187" r="84" fill="url(#photoStairs)" role="img" aria-label="Photo of an accessible stairway and ramp with handrails outside a modern building"/>

    <path d="M520,171 H712 V400 C640,420 560,450 520,470 Z" fill="url(#photoPerson)" role="img" aria-label="Photo of a smiling businessman in a suit presenting with an open hand"/>
    <path d="M477,150 C540,230 620,260 690,270 C705,300 712,330 712,350 C700,310 650,290 600,280 C540,260 500,220 477,180 Z" fill="#acd036" opacity=".9"/>
    <path d="M477,440 C560,400 650,390 712,350 V490 H477 Z" fill="url(#navyFill)"/>
    <path d="M477,440 C560,400 650,390 712,350 V362 C650,400 560,410 477,452 Z" fill="#acd036"/>

    <rect x="0" y="490" width="237" height="13" fill="#acd036"/>
    <rect x="237" y="490" width="238" height="13" fill="#0a2f7a"/>
    <rect x="475" y="490" width="237" height="13" fill="#acd036"/>
  </svg>

  <p class="copy" style="left:265px;top:28px">Lorem ipsum dolor sit amet, consectetur adipiscing elit. Maecenas vitae dfvarius libero. Morbi varius enim ultricdffdfes ultrices volutpat. Praesent dfdfdfviverra auctor sagittis. Aliquam erat volutpat.</p>

  <div class="tab tab--green" style="left:0;top:247px">Lorem ipsum</div>
  <p class="copy" style="left:28px;top:296px">Lorem ipsum dolor sit amet, consectetur adipiscing elit. Maecenas vitae dfvarius libero. Morbi varius enim ultricdffdfes ultrices volutpat. Praesent dfdfdfviverra auctor sagittis. Aliquam erat volutpat.</p>
  <div class="tab tab--green" style="left:0;top:373px">Lorem ipsum</div>
  <p class="copy" style="left:28px;top:419px">Lorem ipsum dolor sit amet, consectetur adipiscing elit. Maecenas vitae dfvarius libero. Morbi varius enim ultricdffdfes ultrices volutpat. Praesent dfdfdfviverra auctor sagittis. Aliquam erat volutpat.</p>

  <div class="contact" style="top:364px">
    <h2 class="contact__title">CONTACT US</h2>
    <p>Call: , 8005172943</p>
    <p>E-Mail: info@email.com</p>
    <p>Lorem ipsum dolor sit amet<br>45/78/44, lorem street<br>License #2004738</p>
  </div>

  <div class="brand">
    <span class="brand__mark"></span>
    <span class="brand__name">Summit Build</span>
  </div>
  <div class="cover-title">LOREM IPSUM</div>
  <div class="cover-web">www.website.com</div>
</section>

<section class="sheet sheet--inside">
  <svg class="sheet__art" viewBox="0 0 712 503" xmlns="http://www.w3.org/2000/svg">
    <defs>
      <linearGradient id="greenPanel2" x1="0" y1="0" x2="0" y2="1">
        <stop offset="0" stop-color="#9fcc2e"/><stop offset=".5" stop-color="#c4e84c"/><stop offset="1" stop-color="#9fcc2e"/>
      </linearGradient>
      <linearGradient id="navyFill2" x1="0" y1="0" x2="1" y2="1">
        <stop offset="0" stop-color="#0a2f7a"/><stop offset="1" stop-color="#0355a3"/>
      </linearGradient>
      <linearGradient id="photoWall" x1="0" y1="0" x2="0" y2="1">
        <stop offset="0" stop-color="#cdb596"/><stop offset=".7" stop-color="#b59c7f"/><stop offset="1" stop-color="#8e8a84"/>
      </linearGradient>
      <linearGradient id="photoStalls" x1="0" y1="0" x2="0" y2="1">
        <stop offset="0" stop-color="#b7cde4"/><stop offset=".3" stop-color="#7d8f74"/><stop offset=".45" stop-color="#2c333b"/><stop offset="1" stop-color="#3a7fd0"/>
      </linearGradient>
      <linearGradient id="photoStriping" x1="0" y1="0" x2="0" y2="1">
        <stop offset="0" stop-color="#c8d8e6"/><stop offset=".35" stop-color="#a89c86"/><stop offset=".5" stop-color="#2a2d31"/><stop offset="1" stop-color="#1e2125"/>
      </linearGradient>
    </defs>

    <rect x="238" y="0" width="237" height="503" fill="url(#greenPanel2)"/>
    <path d="M438,203 C450,250 475,265 475,265 V503 H238 V440 C300,410 360,395 400,360 C440,320 420,260 438,203 Z" fill="url(#navyFill2)"/>
    <path d="M238,425 C300,405 350,390 390,360 C430,330 425,260 438,203 C420,260 420,320 380,350 C340,380 290,395 238,410 Z" fill="#ffffff" opacity=".85"/>
    <circle cx="356" cy="332" r="90" fill="#ffffff" opacity=".9"/>
    <circle cx="356" cy="332" r="85" fill="url(#photoStalls)" role="img" aria-label="Photo of a newly striped parking row with blue accessible parking stalls"/>

    <path d="M0,237 C30,330 140,340 237,430 V503 H0 Z" fill="url(#photoWall)" role="img" aria-label="Photo of a concrete accessible ramp with metal handrails beside a building"/>
    <path d="M0,230 C30,320 140,335 237,420 V432 C140,350 30,340 0,250 Z" fill="#acd036"/>
    <path d="M0,250 C40,330 150,345 237,432 V440 C150,360 30,345 0,262 Z" fill="#0a2f7a"/>

    <path d="M475,305 C560,320 660,330 712,375 V503 H475 Z" fill="url(#photoStriping)" role="img" aria-label="Photo of crews painting new stall lines across a large parking lot"/>
    <path d="M438,203 C470,265 560,300 640,315 C680,325 705,345 712,375 C690,345 650,335 600,325 C530,310 470,280 438,203 Z" fill="url(#navyFill2)"/>
    <path d="M475,300 C560,320 660,325 712,362 V372 C660,340 560,330 475,312 Z" fill="#acd036"/>
  </svg>

  <div class="tab tab--green" style="left:0;top:30px">Lorem ipsum</div>
  <p class="copy" style="left:21px;top:78px">Lorem ipsum dolor sit amet, consectetur adipiscing elit. Maecenas vitae dfvarius libero. Morbi varius enim ultricdffdfes ultrices volutpat. Praesent dfdfdfviverra auctor sagittis. Aliquam erat volutpat.</p>
  <div class="tab tab--green" style="left:0;top:154px">Lorem ipsum</div>
  <p class="copy" style="left:21px;top:202px">Lorem ipsum dolor sit amet, consectetur adipiscing elit. Maecenas vitae dfvarius libero. Morbi varius enim ultricdffdfes ultrices volutpat. Praesent dfdfdfviverra auctor sagittis. Aliquam erat volutpat.</p>

  <h2 class="feature-title">LOREM IPSUM</h2>
  <p class="copy" style="left:264px;top:66px">Lorem ipsum dolor sit amet, consectetur adipiscing elit. Maecenas vitae dfvarius libero. Morbi varius enim ultricdffdfes ultrices volutpat. Praesent dfdfdfviverra auctor sagittis. Aliquam erat volutpat.</p>
  <p class="copy" style="left:264px;top:133px">Lorem ipsum dolor sit amet, consectetur adipiscing elit. Maecenas vitae dfvarius libero. Morbi varius enim ultricdffdfes ultrices volutpat. Praesent dfdfdfviverra auctor sagittis. Aliquam erat volutpat.</p>
  <div class="back-contact back-contact__title">CONTACT US</div>
  <div class="back-contact back-contact__phone">Call: 8005172943</div>

  <div class="tab tab--navy" style="left:475px;top:29px">Lorem ipsum</div>
  <p class="copy" style="left:498px;top:78px">Lorem ipsum dolor sit amet, consectetur adipiscing elit. Maecenas vitae dfvarius libero. Morbi varius enim ultricdffdfes ultrices volutpat. Praesent dfdfdfviverra auctor sagittis. Aliquam erat volutpat.</p>
  <div class="tab tab--navy" style="left:475px;top:159px">Lorem ipsum</div>
  <p class="copy" style="left:498px;top:203px">Lorem ipsum dolor sit amet, consectetur adipiscing elit. Maecenas vitae dfvarius libero. Morbi varius enim ultricdffdfes ultrices volutpat. Praesent dfdfdfviverra auctor sagittis. Aliquam erat volutpat.</p>
</section>

</body>
</html>
```